New Business Card Design Project

double sided business cards. i would like to design a business card with the logo attached . that logo being centered on 1 side and then my info on the other.

Boyd Whitfield CEO
Phone# 334-571-2806
Boyd@brightoakupkeep.com

Contact Information for Business Card

double sided one side the Logo attached below that saying Home Maintenance and Repair Specialists then on back my info Boyd Whitfield CEO Home Maintenance Specialist Phone# 334-571-2806 Boyd@brightoakupkeep.com

Font styles to use
Serif

Colors
0054AA
0677BA
7BADD7
CADEEF
E8F1F8
FFC000
F8CF3A
FAE287
FDF2CF
FEFAEE

Requirements
Must have
• double sided logo attached on one side with colors blue and gold. black background info on the other side

```html
<!DOCTYPE html>
<html lang="en">
<head>
<meta charset="utf-8">
<title>Bright Oak Upkeep — Business Card</title>
<link rel="stylesheet" href="https://fonts.googleapis.com/css2?family=Roboto:wght@400;500;700&display=swap">
<style>
  :root{
    --blue-deep:#0054AA;
    --blue:#0677BA;
    --blue-soft:#7BADD7;
    --blue-pale:#CADEEF;
    --blue-mist:#E8F1F8;
    --gold:#F8CF3A;
    --gold-deep:#FFC000;
    --ink:#1f2a33;
    --rule:#5a5f66;
    --page:#ffffff;
  }
  *{margin:0;padding:0;box-sizing:border-box;}
  html,body{width:800px;height:1200px;overflow:hidden;background:var(--page);}
  body{position:relative;font-family:"Roboto",Arial,sans-serif;}

  .card{
    position:absolute;left:80px;width:640px;height:366px;overflow:hidden;
    box-shadow:6px 8px 10px rgba(0,0,0,.45);
  }
  .card--info{top:204px;background:var(--blue-mist);}
  .card--brand{top:630px;background:var(--blue);}

  .tagline{
    position:absolute;left:0;width:100%;text-align:center;
    font-weight:700;font-size:24px;letter-spacing:.2px;
    background:linear-gradient(90deg,#ffffff 0%,#ffffff 45%,var(--blue-pale) 75%,var(--blue-soft) 100%);
    -webkit-background-clip:text;background-clip:text;color:transparent;
    text-shadow:0 1px 1px rgba(0,0,0,.08);
  }

  /* info side */
  .top-band{position:absolute;left:0;top:0;width:100%;height:100px;background:var(--blue);}
  .top-band .tagline{top:36px;}
  .stripe-blue{position:absolute;left:0;top:108px;width:268px;height:63px;background:var(--blue);}
  .stripe-gold{position:absolute;left:330px;top:108px;width:310px;height:63px;background:var(--gold);}
  .brand-dot{position:absolute;border-radius:50%;background:var(--blue);}
  .card--info .brand-dot{left:274px;top:110px;width:52px;height:52px;}
  .brand-name{
    position:absolute;left:0;width:100%;text-align:center;
    font-weight:700;letter-spacing:1px;
  }
  .card--info .brand-name{top:178px;font-size:28px;color:var(--blue);}

  .person{position:absolute;right:405px;top:262px;text-align:right;}
  .person__name{font-size:26px;font-weight:700;color:var(--blue);line-height:1.1;}
  .person__title{font-size:26px;font-weight:700;color:var(--gold);line-height:1.15;}
  .divider{position:absolute;left:274px;top:252px;width:1px;height:88px;background:var(--rule);}
  .contact{position:absolute;left:313px;top:262px;list-style:none;}
  .contact li{display:flex;align-items:center;height:20px;margin-bottom:14px;font-size:15px;color:var(--ink);}
  .contact svg{width:13px;height:13px;margin-right:8px;flex:none;}

  /* brand side */
  .card--brand .brand-dot{left:290px;top:140px;width:60px;height:60px;background:var(--gold);}
  .card--brand .brand-name{top:212px;font-size:30px;color:#ffffff;}
  .card--brand .tagline{top:290px;}
</style>
</head>
<body>

<section class="card card--info" aria-label="Contact side">
  <div class="top-band"><p class="tagline">Home Maintenance &amp; Repair Specialists</p></div>
  <div class="stripe-blue"></div>
  <div class="stripe-gold"></div>
  <span class="brand-dot"></span>
  <p class="brand-name">BRIGHT OAK UPKEEP</p>

  <div class="person">
    <p class="person__name">Boyd Whitfield</p>
    <p class="person__title">CEO</p>
  </div>
  <div class="divider"></div>
  <ul class="contact">
    <li>
      <svg viewBox="0 0 24 24" aria-hidden="true"><path fill="#0677BA" d="M6.6 10.8a15.1 15.1 0 0 0 6.6 6.6l2.2-2.2a1 1 0 0 1 1-.25 11.4 11.4 0 0 0 3.6.57 1 1 0 0 1 1 1V20a1 1 0 0 1-1 1A17 17 0 0 1 3 4a1 1 0 0 1 1-1h3.5a1 1 0 0 1 1 1c0 1.25.2 2.45.57 3.57a1 1 0 0 1-.25 1z"/></svg>
      334-571-2806
    </li>
    <li>
      <svg viewBox="0 0 24 24" aria-hidden="true"><rect x="2" y="5" width="20" height="14" fill="#0677BA"/><path d="M2 5l10 8 10-8" fill="none" stroke="#E8F1F8" stroke-width="1.8"/></svg>
      Boyd@brightoakupkeep.com
    </li>
  </ul>
</section>

<section class="card card--brand" aria-label="Brand side">
  <span class="brand-dot"></span>
  <p class="brand-name">BRIGHT OAK UPKEEP</p>
  <p class="tagline">Home Maintenance &amp; Repair Specialists</p>
</section>

</body>
</html>
```